Stand Tall Always needs a book cover design

I need a book cover design for the following title:
Stand Tall Always-Grow a Bold Captain
Family methods from Cradle through Elder Years
by Dr. Martin P. Olund
I am interviewing a number of strong Canadian Leaders-specifically with regard to their experience of being parented. The book is a reaction today of parents having no backbone, no will nor ability to discipline their children. Many parents want to make a change but don't know how to.
Updates
Title should be "Stand Tall Always-Grow a Bold Captain" the rest is correct Added Wednesday, November 11, 2015
Here is an example of what we would need on the back cover in text only.
What does it take to raise a strong leader? Psychologist Dr. Martin P. Olund provides you with 6 must do strategies based on his 26 years of clinical experience and the interview of 6 strong leaders for this book. Strategies that you can start using today to insure your child’s success.
Target Market(s)
parents and grandparents
Requirements
Must have
- a way to communicate strength in parenting

```html
<!DOCTYPE html>
<html lang="en">
<head>
<meta charset="UTF-8">
<title>Stand Tall Always – Book Cover</title>
<link rel="stylesheet" href="https://fonts.googleapis.com/css2?family=Bebas+Neue&family=Open+Sans:wght@400&display=swap">
<style>
  :root {
    --paper: #d9dee1;
    --paper-light: #e8ecee;
    --paper-dark: #c7cdd1;
    --title-blue: #2f86c6;
    --ink: #1c1c1c;
    --photo-light: #eef1f2;
    --photo-mid: #c9b5a0;
    --photo-dark: #5c4a3c;
  }
  * { margin: 0; padding: 0; box-sizing: border-box; }
  html, body { width: 1200px; height: 860px; overflow: hidden; background: var(--paper); }
  .cover {
    position: relative;
    width: 1200px;
    height: 860px;
    background:
      radial-gradient(ellipse at 70% 40%, var(--paper-light) 0%, transparent 60%),
      radial-gradient(ellipse at 20% 80%, var(--paper-dark) 0%, transparent 55%),
      linear-gradient(160deg, var(--paper-light), var(--paper) 50%, var(--paper-dark));
    overflow: hidden;
  }
  .back-blurb {
    position: absolute;
    left: 35px;
    top: 198px;
    width: 500px;
    font-family: "Open Sans", sans-serif;
    font-size: 20.5px;
    line-height: 31px;
    color: var(--ink);
    text-align: justify;
  }
  .spine {
    position: absolute;
    left: 580px;
    top: 68px;
    width: 30px;
    height: 720px;
  }
  .spine-title, .spine-author {
    position: absolute;
    left: 0;
    writing-mode: vertical-rl;
    font-family: "Bebas Neue", sans-serif;
    white-space: nowrap;
  }
  .spine-title {
    top: 0;
    font-size: 25px;
    color: var(--title-blue);
    letter-spacing: 0.5px;
  }
  .spine-author {
    top: 522px;
    font-size: 25px;
    color: var(--ink);
    letter-spacing: 1.5px;
  }
  .front {
    position: absolute;
    left: 615px;
    top: 0;
    width: 585px;
    height: 860px;
    text-align: center;
  }
  .front-title {
    position: relative;
    z-index: 2;
    margin-top: 76px;
    font-family: "Bebas Neue", sans-serif;
    font-weight: 400;
    color: var(--title-blue);
    font-size: 74px;
    line-height: 62px;
  }
  .front-title .title-line { display: block; }
  .front-subtitle {
    position: relative;
    z-index: 2;
    margin-top: 36px;
    font-family: "Bebas Neue", sans-serif;
    font-size: 27px;
    letter-spacing: 2.6px;
    line-height: 28px;
    color: var(--ink);
  }
  .front-photo {
    position: absolute;
    z-index: 1;
    left: 100px;
    top: 385px;
    width: 385px;
    height: 390px;
    background:
      radial-gradient(ellipse at 50% 35%, var(--photo-dark) 0%, var(--photo-mid) 30%, transparent 62%),
      radial-gradient(ellipse at 50% 80%, var(--photo-light) 0%, transparent 60%);
  }
  .front-author {
    position: absolute;
    left: 0;
    right: 0;
    top: 782px;
    font-family: "Bebas Neue", sans-serif;
    font-size: 40px;
    letter-spacing: 4px;
    color: var(--ink);
  }
</style>
</head>
<body>
<main class="cover">
  <section class="back">
    <p class="back-blurb">What does it take to raise a strong leader? Psychologist Dr. Martin P. Olund provides you with 6 must do strategies based on his 26 years of clinical experience and the interview of 6 strong leaders for this book. Strategies that you can start using today to insure your child’s success.</p>
  </section>

  <section class="spine">
    <span class="spine-title">STAND TALL ALWAYS GROW A BOLD CAPTAIN</span>
    <span class="spine-author">DR. MARTIN P. OLUND</span>
  </section>

  <section class="front">
    <h1 class="front-title">
      <span class="title-line">STAND TALL ALWAYS</span>
      <span class="title-line">GROW A BOLD</span>
      <span class="title-line">CAPTAIN</span>
    </h1>
    <p class="front-subtitle">FAMILY METHODS FROM CRADLE THROUGH<br>ELDER YEARS</p>
    <div class="front-photo" role="img" aria-label="Photograph of a young child seen from behind, wearing a white tank top, raising both fists in a show of strength against a bright backlight"></div>
    <p class="front-author">DR. MARTIN P. OLUND</p>
  </section>
</main>
</body>
</html>
```